Talvoro Equity LLC

Need Professional Business cards for New Investment Fund

Target Market(s)

High Quality investors

Industry/Entity Type

Financial

Contact Information for Business Card

Phone Number +1 555 284 6190
Name Milan Dorovsky
Title Fund Manager
email md@FundTalvoro.com
Website www.FundTalvoro.com

Colors

Designer to choose colors to be used in the design.

Requirements
Must have
• Must have our Logo and all of the above. Must be made so lettering and loge can be raised

```html
<!DOCTYPE html>
<html lang="en">
<head>
<meta charset="utf-8">
<title>Talvoro Equity LLC – Business Card</title>
<link href="https://fonts.googleapis.com/css2?family=Montserrat:wght@400;600;700&display=swap" rel="stylesheet">
<style>
  :root {
    --bg: #141414;
    --card: #2b2b2c;
    --card-back: #262627;
    --pattern: #303031;
    --green: #33e01f;
    --white: #f4f4f4;
    --rule: #8a8a8a;
  }
  * { margin: 0; padding: 0; box-sizing: border-box; }
  html, body {
    width: 1200px; height: 900px; overflow: hidden;
    background: radial-gradient(ellipse at 50% 45%, #262626 0%, var(--bg) 70%);
    font-family: "Montserrat", sans-serif;
  }
  .stage {
    position: relative; width: 1200px; height: 900px;
    display: flex; justify-content: center; align-items: center; gap: 100px;
  }
  .card {
    width: 350px; height: 600px;
    border: 3px solid var(--green);
    border-radius: 2px;
    position: relative;
    box-shadow: 0 20px 40px rgba(0,0,0,.55);
  }
  .card-front { background: var(--card); }
  .card-back { background: var(--card-back); }

  .brand {
    position: absolute; top: 120px; left: 0; right: 0;
    display: flex; justify-content: center; align-items: center; gap: 12px;
  }
  .brand-mark { width: 26px; height: 26px; background: var(--green); }
  .brand-name {
    color: var(--white); font-weight: 700; font-size: 34px; letter-spacing: 1px;
  }

  .contact {
    position: absolute; left: 0; right: 0; bottom: 70px;
    text-align: center; color: var(--white);
  }
  .contact-name {
    color: var(--green); font-weight: 700; font-size: 21px; letter-spacing: .5px;
    text-transform: uppercase;
  }
  .contact-title { font-size: 15px; margin-top: 4px; }
  .icon-row {
    display: flex; align-items: center; justify-content: center; gap: 6px;
    margin: 12px auto 12px; width: 240px;
  }
  .icon-row .rule { flex: 1; height: 1px; background: var(--rule); }
  .icon { width: 20px; height: 20px; display: block; }
  .contact-line { font-size: 15px; line-height: 1.45; }

  .pattern {
    position: absolute; inset: 0;
    background: repeating-linear-gradient(135deg, var(--card-back) 0 18px, var(--pattern) 18px 36px);
  }
  .back-brand {
    position: absolute; left: 0; right: 0; top: 50%; transform: translateY(-50%);
    display: flex; justify-content: center; align-items: center; gap: 8px;
  }
  .back-brand .brand-mark { width: 12px; height: 12px; }
  .back-brand .brand-name { font-size: 18px; }
</style>
</head>
<body>
<main class="stage">
  <section class="card card-front" aria-label="Card front">
    <div class="brand">
      <span class="brand-mark"></span>
      <span class="brand-name">Talvoro</span>
    </div>
    <div class="contact">
      <h1 class="contact-name">Milan Dorovsky</h1>
      <p class="contact-title">Fund Manager</p>
      <div class="icon-row">
        <span class="rule"></span>
        <svg class="icon" viewBox="0 0 20 20" aria-label="Phone"><circle cx="10" cy="10" r="10" fill="#33e01f"/><path d="M6.5 5.5l2 0 1 2.5-1.3 1a6 6 0 0 0 3 3l1-1.3 2.5 1v2a1 1 0 0 1-1 1A8 8 0 0 1 5.5 6.5a1 1 0 0 1 1-1z" fill="#2b2b2c"/></svg>
        <svg class="icon" viewBox="0 0 20 20" aria-label="Email"><circle cx="10" cy="10" r="10" fill="#33e01f"/><rect x="5" y="6.5" width="10" height="7" fill="#2b2b2c"/><path d="M5 6.5l5 4 5-4" fill="none" stroke="#33e01f" stroke-width="1"/></svg>
        <svg class="icon" viewBox="0 0 20 20" aria-label="Website"><circle cx="10" cy="10" r="10" fill="#33e01f"/><g fill="none" stroke="#2b2b2c" stroke-width="1.2"><circle cx="10" cy="10" r="5"/><ellipse cx="10" cy="10" rx="2.2" ry="5"/><path d="M5 10h10"/></g></svg>
        <span class="rule"></span>
      </div>
      <p class="contact-line">+1 555 284 6190</p>
      <p class="contact-line">md@FundTalvoro.com</p>
      <p class="contact-line">www.FundTalvoro.com</p>
    </div>
  </section>

  <section class="card card-back" aria-label="Card back">
    <div class="pattern" role="img" aria-label="Repeating tonal brand pattern"></div>
    <div class="back-brand">
      <span class="brand-mark"></span>
      <span class="brand-name">Talvoro</span>
    </div>
  </section>
</main>
</body>
</html>
```